Business Card for Willowcrest Terrain Advisors

We need a business card for Willowcrest Terrain Advisors. The company website address is provided below. The company logo is attached. We provide specialized permafrost services to the mining, transportation, and oil & gas industries. The card should be prepared for:
Dominic Halloway, PhD.
Willowcrest Terrain Advisors
PO Box 418529
Birch Hollow, Alaska 99612
Direct: +1-907-555-2964
Email: dhalloway@terrainadvisors-example.com
Website: www.willowcrestterrainadvisors-example.com

```html
<!DOCTYPE html>
<html lang="en">
<head>
<meta charset="utf-8">
<title>Willowcrest Terrain Advisors – Business Card</title>
<link href="https://fonts.googleapis.com/css2?family=Montserrat:wght@400;500;600&display=swap" rel="stylesheet">
<style>
  :root {
    --page: #ffffff;
    --red: #b81c24;
    --red-deep: #9e151c;
    --black: #141414;
    --ink-light: #ffffff;
    --divider: rgba(255,255,255,0.45);
  }
  html, body {
    margin: 0;
    padding: 0;
    width: 1200px;
    height: 1125px;
    overflow: hidden;
    background: var(--page);
    font-family: "Montserrat", Arial, sans-serif;
  }
  .canvas {
    position: relative;
    width: 1200px;
    height: 1125px;
  }
  .card {
    position: absolute;
    left: 204px;
    width: 788px;
    height: 450px;
    overflow: hidden;
  }
  .card-front {
    top: 88px;
    background: radial-gradient(ellipse at 50% 45%, var(--red) 0%, var(--red-deep) 100%);
  }
  .card-back {
    top: 580px;
    background: radial-gradient(ellipse at 50% 40%, #1c1c1c 0%, var(--black) 100%);
    color: var(--ink-light);
  }
  .wordmark {
    position: absolute;
    text-align: center;
    color: var(--ink-light);
    font-weight: 500;
    text-transform: uppercase;
  }
  .wordmark .wordmark-main {
    display: block;
    letter-spacing: 3px;
  }
  .wordmark .wordmark-sub {
    display: block;
    letter-spacing: 7px;
  }
  .card-front .wordmark {
    left: 0;
    width: 788px;
    top: 322px;
  }
  .card-front .wordmark-main { font-size: 38px; line-height: 44px; }
  .card-front .wordmark-sub { font-size: 14px; line-height: 22px; margin-top: 2px; }
  .card-back .wordmark {
    left: 20px;
    width: 282px;
    top: 184px;
  }
  .card-back .wordmark-main { font-size: 25px; line-height: 30px; letter-spacing: 2px; }
  .card-back .wordmark-sub { font-size: 10px; line-height: 16px; letter-spacing: 4px; margin-top: 2px; }
  .divider {
    position: absolute;
    left: 337px;
    top: 87px;
    width: 1px;
    height: 266px;
    background: linear-gradient(to bottom, transparent, var(--divider) 30%, var(--divider) 70%, transparent);
  }
  .contact-name {
    position: absolute;
    left: 385px;
    top: 110px;
    margin: 0;
    font-size: 25px;
    font-weight: 600;
    line-height: 32px;
  }
  .contact-company {
    position: absolute;
    left: 384px;
    top: 147px;
    margin: 0;
    font-size: 16px;
    font-weight: 500;
  }
  .contact-list {
    position: absolute;
    left: 385px;
    top: 190px;
    margin: 0;
    padding: 0;
    list-style: none;
  }
  .contact-list li {
    display: flex;
    align-items: center;
    height: 38px;
    font-size: 16px;
    font-weight: 500;
  }
  .contact-list li.phone { font-size: 21px; height: 40px; }
  .contact-list svg {
    width: 22px;
    height: 22px;
    margin-right: 13px;
    flex: none;
  }
  .address {
    position: absolute;
    left: 0;
    width: 788px;
    top: 385px;
    margin: 0;
    text-align: center;
    font-size: 21px;
    font-weight: 600;
  }
</style>
</head>
<body>
<div class="canvas">

  <section class="card card-front">
    <div class="wordmark">
      <span class="wordmark-main">Willowcrest</span>
      <span class="wordmark-sub">Terrain Advisors</span>
    </div>
  </section>

  <section class="card card-back">
    <div class="wordmark">
      <span class="wordmark-main">Willowcrest</span>
      <span class="wordmark-sub">Terrain Advisors</span>
    </div>

    <div class="divider"></div>

    <h1 class="contact-name">Dominic Halloway, PhD.</h1>
    <p class="contact-company">Willowcrest Terrain Advisors</p>

    <ul class="contact-list">
      <li class="phone">
        <svg viewBox="0 0 24 24" aria-hidden="true">
          <path fill="#c8202a" d="M6.6 10.8c1.4 2.8 3.8 5.1 6.6 6.6l2.2-2.2c.3-.3.7-.4 1-.2 1.1.4 2.3.6 3.6.6.6 0 1 .4 1 1V20c0 .6-.4 1-1 1C10.6 21 3 13.4 3 4c0-.6.4-1 1-1h3.5c.6 0 1 .4 1 1 0 1.3.2 2.5.6 3.6.1.3 0 .7-.2 1z"/>
          <path fill="none" stroke="#c8202a" stroke-width="1.6" d="M14 3.5a7 7 0 0 1 6.5 6.5M14 7a3.5 3.5 0 0 1 3 3"/>
        </svg>
        +1-907-555-2964
      </li>
      <li class="email">
        <svg viewBox="0 0 24 24" aria-hidden="true">
          <rect x="2" y="5" width="20" height="14" rx="1.5" fill="#c8202a"/>
          <path d="M2.5 6l9.5 7 9.5-7" fill="none" stroke="#141414" stroke-width="1.5"/>
        </svg>
        dhalloway@terrainadvisors-example.com
      </li>
      <li class="web">
        <svg viewBox="0 0 24 24" aria-hidden="true">
          <g fill="none" stroke="#c8202a" stroke-width="1.7">
            <circle cx="12" cy="12" r="9"/>
            <ellipse cx="12" cy="12" rx="4" ry="9"/>
            <path d="M3 12h18M4.5 7.5h15M4.5 16.5h15"/>
          </g>
        </svg>
        www.willowcrestterrainadvisors-example.com
      </li>
    </ul>

    <p class="address">PO Box 418529 Birch Hollow, Alaska 99612</p>
  </section>

</div>
</body>
</html>
```